Gaming Headset Packaging Design

We would like a gaming window box style packaging design for our gaming headset.

We want to use the packaging for 2-3 of our gaming headphone series and hence we would not like to put any product pictures on the packaging.

Size: (enclosed die-cut drawing) please feel free to modify the shape of the window
Material: E Flute Paper box
Type: Window Box style
Design features we prefer: gaming, playful, creative, trendy, High tech.
Requirement: AI file is preferred

Enclosed are a detailed description along with competitor designs and existing die-cut drawing (AI format) for your reference.

Any further questions, please feel free to ask.

```html
<!DOCTYPE html>
<html lang="en">
<head>
<meta charset="utf-8">
<title>Pro Gaming Headset 7.1 – Window Box Dieline</title>
<link rel="stylesheet" href="https://fonts.googleapis.com/css2?family=Barlow+Condensed:ital,wght@0,500;0,600;1,600&family=Merriweather:wght@900&family=Lato:wght@400;700;900&display=swap">
<style>
  :root {
    --paper: #ffffff;
    --dim-line: #8fd6e2;
    --dim-text: #5fb9c8;
    --plum: #4d0c5c;
    --violet: #3a1a8a;
    --navy: #1e2a7e;
    --ink-dark: #16093a;
    --window: #bcbdbf;
    --info-panel: rgba(205, 175, 230, 0.62);
    --white: #ffffff;
    --logo-ink: #2a0d6e;
    --glue-stroke: #9a9a9a;
  }
  html, body {
    margin: 0;
    width: 1200px;
    height: 977px;
    overflow: hidden;
    background: var(--paper);
  }
  .dieline { display: block; width: 1200px; height: 977px; }
  .dim-line { stroke: var(--dim-line); stroke-width: 1; fill: none; }
  .dim-label { font-family: 'Barlow Condensed', sans-serif; font-size: 10px; fill: var(--dim-text); }
  .fold { stroke: #0b0520; stroke-width: 0.8; stroke-dasharray: 3 2; fill: none; opacity: .7; }
  .side-title { font-family: 'Barlow Condensed', sans-serif; font-weight: 600; font-size: 21px; fill: var(--white); }
  .side-item { font-family: 'Barlow Condensed', sans-serif; font-weight: 500; font-size: 11.5px; fill: var(--white); }
  .range-small { font-family: 'Merriweather', serif; font-weight: 900; font-size: 18px; fill: var(--white); }
  .range-large { font-family: 'Merriweather', serif; font-weight: 900; font-size: 39px; fill: var(--white); }
  .features-title { font-family: 'Barlow Condensed', sans-serif; font-weight: 600; font-size: 20px; fill: var(--white); }
  .feature-item { font-family: 'Lato', sans-serif; font-weight: 900; font-size: 11.5px; fill: var(--white); }
  .logo-word { font-family: 'Lato', sans-serif; font-weight: 900; font-size: 18px; fill: var(--logo-ink); }
  .info-title { font-family: 'Barlow Condensed', sans-serif; font-weight: 600; font-style: italic; font-size: 19px; fill: var(--white); }
  .info-item { font-family: 'Barlow Condensed', sans-serif; font-weight: 500; font-size: 7.6px; fill: var(--white); }
  .info-head { font-family: 'Barlow Condensed', sans-serif; font-weight: 600; font-size: 10px; fill: var(--white); }
  .placeholder-label { font-family: 'Barlow Condensed', sans-serif; font-weight: 500; font-size: 9px; fill: #333; }
</style>
</head>
<body>
<svg class="dieline" viewBox="0 0 1500 1222" preserveAspectRatio="none" xmlns="http://www.w3.org/2000/svg">
  <defs>
    <linearGradient id="grad-plum-navy" x1="0" y1="0" x2="1" y2="1">
      <stop offset="0" stop-color="#3c0a52"/>
      <stop offset="0.45" stop-color="#3a137a"/>
      <stop offset="1" stop-color="#1f2a80"/>
    </linearGradient>
    <linearGradient id="grad-lid" x1="0" y1="0" x2="1" y2="0.8">
      <stop offset="0" stop-color="#3d0b4f"/>
      <stop offset="0.3" stop-color="#4f0f65"/>
      <stop offset="1" stop-color="#1f2a80"/>
    </linearGradient>
    <linearGradient id="grad-bottom" x1="0" y1="0" x2="1" y2="0">
      <stop offset="0" stop-color="#3a0b50"/>
      <stop offset="0.35" stop-color="#4c0e62"/>
      <stop offset="0.65" stop-color="#2a1a7a"/>
      <stop offset="1" stop-color="#1e2a7e"/>
    </linearGradient>
    <radialGradient id="glow-side" cx="0.55" cy="0.5" r="0.6">
      <stop offset="0" stop-color="#2c2390"/>
      <stop offset="0.6" stop-color="#26125e"/>
      <stop offset="1" stop-color="#170934"/>
    </radialGradient>
    <radialGradient id="glow-front" cx="0.6" cy="0.45" r="0.7">
      <stop offset="0" stop-color="#5a1b9a"/>
      <stop offset="0.5" stop-color="#33207e"/>
      <stop offset="1" stop-color="#170934"/>
    </radialGradient>
    <radialGradient id="glow-back" cx="0.45" cy="0.4" r="0.75">
      <stop offset="0" stop-color="#4a1a8a"/>
      <stop offset="0.55" stop-color="#2c1a72"/>
      <stop offset="1" stop-color="#170934"/>
    </radialGradient>
  </defs>

  <!-- Dimension guides -->
  <g class="dimensions">
    <line class="dim-line" x1="160" y1="122" x2="1445" y2="122"/>
    <line class="dim-line" x1="160" y1="114" x2="160" y2="486"/>
    <line class="dim-line" x1="1445" y1="114" x2="1445" y2="130"/>
    <rect x="784" y="115" width="32" height="13" fill="var(--paper)"/>
    <text class="dim-label" x="800" y="126" text-anchor="middle">636.00</text>

    <line class="dim-line" x1="160" y1="148" x2="782" y2="148"/>
    <line class="dim-line" x1="378" y1="140" x2="378" y2="217"/>
    <line class="dim-line" x1="782" y1="140" x2="782" y2="217"/>
    <rect x="252" y="141" width="32" height="13" fill="var(--paper)"/>
    <text class="dim-label" x="268" y="152" text-anchor="middle">108.00</text>
    <rect x="562" y="141" width="32" height="13" fill="var(--paper)"/>
    <text class="dim-label" x="578" y="152" text-anchor="middle">200.00</text>

    <line class="dim-line" x1="82" y1="217" x2="82" y2="1127"/>
    <line class="dim-line" x1="74" y1="217" x2="382" y2="217"/>
    <line class="dim-line" x1="74" y1="1127" x2="163" y2="1127"/>
    <rect x="75" y="656" width="14" height="36" fill="var(--paper)"/>
    <text class="dim-label" transform="translate(85 674) rotate(-90)" text-anchor="middle">450.00</text>

    <line class="dim-line" x1="102" y1="486" x2="102" y2="970"/>
    <line class="dim-line" x1="96" y1="486" x2="160" y2="486"/>
    <line class="dim-line" x1="96" y1="970" x2="160" y2="970"/>
    <rect x="95" y="712" width="14" height="36" fill="var(--paper)"/>
    <text class="dim-label" transform="translate(105 730) rotate(-90)" text-anchor="middle">240.00</text>
  </g>

  <!-- Top lid and dust flaps -->
  <g class="top-flaps">
    <path d="M378 486 V268 H382 V235 Q382 217 400 217 H760 Q778 217 778 235 V268 H782 V486 Z" fill="url(#grad-lid)"/>
    <path class="fold" d="M382 268 H402 M402 268 V272 H540 V268 H620 V272 H758 V268 H778"/>
    <polygon points="192,365 372,365 372,486 163,486 163,465" fill="url(#grad-plum-navy)"/>
    <polygon points="789,365 968,365 996,465 996,486 789,486" fill="url(#grad-plum-navy)"/>
    <path d="M1163 486 V456 Q1163 446 1173 446 H1231 Q1241 446 1241 456 V486 Z" fill="#3a1a8a"/>
  </g>

  <!-- Bottom flaps -->
  <g class="bottom-flaps">
    <polygon points="163,970 378,970 378,1065 270,1065 267,1127 163,1127" fill="url(#grad-plum-navy)"/>
    <polygon points="382,970 778,970 778,1127 688,1127 688,1080 472,1080 472,1127 382,1127" fill="url(#grad-bottom)"/>
    <polygon points="789,970 996,970 996,1127 895,1127 893,1080 789,975" fill="url(#grad-plum-navy)"/>
    <polygon points="1000,970 1405,970 1308,1075 1308,1127 1097,1127 1097,1075" fill="url(#grad-plum-navy)"/>
  </g>

  <!-- Glue flap -->
  <polygon class="glue-flap" points="1405,486 1445,500 1445,955 1405,970" fill="var(--paper)" stroke="var(--glue-stroke)" stroke-width="1"/>

  <!-- Body panels -->
  <g class="body-panels">
    <rect x="160" y="486" width="218" height="484" fill="url(#glow-side)"/>
    <rect x="378" y="486" width="404" height="484" fill="url(#glow-front)" role="img" aria-label="Faceted geometric texture in purple and blue tones"/>
    <rect x="782" y="486" width="218" height="484" fill="url(#glow-side)"/>
    <rect x="1000" y="486" width="405" height="484" fill="url(#glow-back)" role="img" aria-label="Faceted geometric texture in purple and blue tones"/>
    <path class="fold" d="M378 486 V970 M782 486 V970 M1000 486 V970 M160 486 H1405 M160 970 H1405"/>
    <line x1="1163" y1="524" x2="1241" y2="524" stroke="#0b0520" stroke-width="1"/>
  </g>

  <!-- Side panel: specification -->
  <g class="side-spec">
    <text class="side-title" x="188" y="578">Specification:</text>
    <g class="side-item">
      <circle cx="192" cy="598" r="2.2" fill="#fff"/><text class="side-item" x="206" y="602">Headphone Specification</text>
      <circle cx="192" cy="616" r="2.2" fill="#fff"/><text class="side-item" x="206" y="620">Speaker Diameter: Ø40mm</text>
      <circle cx="192" cy="634" r="2.2" fill="#fff"/><text class="side-item" x="206" y="638">Impedance: 32Ω ± 15</text>
      <circle cx="192" cy="653" r="2.2" fill="#fff"/><text class="side-item" x="206" y="657">Sensitivity S.P.L: 113dB ± 3dB</text>
      <circle cx="192" cy="671" r="2.2" fill="#fff"/><text class="side-item" x="206" y="675">Rated Power: 20mW</text>
      <circle cx="192" cy="689" r="2.2" fill="#fff"/><text class="side-item" x="206" y="693">Aggregate capability: 30mW</text>
      <circle cx="192" cy="707" r="2.2" fill="#fff"/><text class="side-item" x="206" y="711">Frequency Response: 20-20kHz</text>
      <circle cx="192" cy="726" r="2.2" fill="#fff"/><text class="side-item" x="206" y="730">Plug Type: 3.</text>
      <circle cx="192" cy="744" r="2.2" fill="#fff"/><text class="side-item" x="206" y="748">Microphone Specification</text>
      <circle cx="192" cy="762" r="2.2" fill="#fff"/><text class="side-item" x="206" y="766">Microphone Unit: Ø6 x 5mm</text>
      <circle cx="192" cy="780" r="2.2" fill="#fff"/><text class="side-item" x="206" y="784">Sensitivity S.P.L 34dB ± 3dB</text>
      <circle cx="192" cy="799" r="2.2" fill="#fff"/><text class="side-item" x="206" y="803">Impedance: &lt;2.2k</text>
      <circle cx="192" cy="817" r="2.2" fill="#fff"/><text class="side-item" x="206" y="821">Frequency Response: 30-16kHz</text>
      <circle cx="192" cy="835" r="2.2" fill="#fff"/><text class="side-item" x="206" y="839">Standard Operating Voltage: 4.5V</text>
      <circle cx="192" cy="854" r="2.2" fill="#fff"/><text class="side-item" x="206" y="858">S/N Ratio: Z 60dB</text>
      <circle cx="192" cy="872" r="2.2" fill="#fff"/><text class="side-item" x="206" y="876">Plug Type: 3.5mm Stereo5mm Stereo</text>
    </g>
  </g>

  <!-- Front panel -->
  <g class="front-panel">
    <circle cx="448" cy="550" r="60" fill="var(--white)"/>
    <text class="logo-word" x="448" y="556" text-anchor="middle">Logo</text>

    <text class="range-small" x="404" y="668">PRO GAMING</text>
    <text class="range-large" x="404" y="709">HEADSET</text>
    <text class="range-large" x="404" y="751">7.1</text>

    <text class="features-title" x="404" y="860">FEATURES:</text>
    <text class="feature-item" x="404" y="882">● Virtual 7.1 Surround Sound</text>
    <text class="feature-item" x="404" y="896">● Dual Drivers on each ear for Accuracy</text>
    <text class="feature-item" x="404" y="910">● 3D Sound Vibration</text>
    <text class="feature-item" x="404" y="924">● Bendable Stainless-Steel headband</text>
    <text class="feature-item" x="404" y="938">● Soft and soothing earpads</text>
  </g>

  <!-- Product window cut-out -->
  <polygon class="product-window" fill="var(--window)"
    points="660,548 870,548 860,555 1000,555 1008,545 1083,545 1120,582 1120,655 1107,672 1107,780 1120,797 1120,920 978,920 985,903 870,903 855,920 626,920 626,748 640,735 640,707 626,695 626,583"/>

  <!-- Back panel information -->
  <g class="back-info">
    <rect x="1127" y="555" width="258" height="338" fill="var(--info-panel)"/>
    <text class="info-title" x="1141" y="590">Specification:</text>

    <g class="info-col-left">
      <text class="info-item" x="1143" y="606">•</text><text class="info-item" x="1155" y="606">Headphone Specification</text>
      <text class="info-item" x="1143" y="616">•</text><text class="info-item" x="1155" y="616">Speaker Diameter: Ø40mm</text>
      <text class="info-item" x="1143" y="627">•</text><text class="info-item" x="1155" y="627">Impedance: 32Ω ± 15</text>
      <text class="info-item" x="1143" y="637">•</text><text class="info-item" x="1155" y="637">Sensitivity S.P.L: 113dB ± 3dB</text>
      <text class="info-item" x="1143" y="647">•</text><text class="info-item" x="1155" y="647">Rated Power: 20mW</text>
      <text class="info-item" x="1143" y="658">•</text><text class="info-item" x="1155" y="658">Aggregate capability: 30mW</text>
      <text class="info-item" x="1143" y="668">•</text><text class="info-item" x="1155" y="668">Frequency Response: 20-20kHz</text>
      <text class="info-item" x="1143" y="678">•</text><text class="info-item" x="1155" y="678">Plug Type: 3.5mm Stereo</text>
    </g>
    <g class="info-col-right">
      <text class="info-item" x="1259" y="606">•</text><text class="info-item" x="1271" y="606">Microphone Specification</text>
      <text class="info-item" x="1259" y="616">•</text><text class="info-item" x="1271" y="616">Microphone Unit: Ø6 x 5mm</text>
      <text class="info-item" x="1259" y="627">•</text><text class="info-item" x="1271" y="627">Sensitivity S.P.L 34dB ± 3dB</text>
      <text class="info-item" x="1259" y="637">•</text><text class="info-item" x="1271" y="637">Impedance: &lt;2.2k</text>
      <text class="info-item" x="1259" y="647">•</text><text class="info-item" x="1271" y="647">Frequency Response: 30-16kHz</text>
      <text class="info-item" x="1259" y="658">•</text><text class="info-item" x="1271" y="658">Standard Operating Voltage: 4.5V</text>
      <text class="info-item" x="1259" y="668">•</text><text class="info-item" x="1271" y="668">S/N Ratio: Z 60dB</text>
      <text class="info-item" x="1259" y="678">•</text><text class="info-item" x="1271" y="678">Plug Type: 3.5mm Stereo</text>
    </g>

    <text class="info-item" x="1141" y="705">Warning: Adjust headphone's sound to a proper volume. Loud sound may</text>
    <text class="info-item" x="1141" y="715">damage your ears. For traffic safety never use the headset while driving.</text>

    <text class="info-item" x="1141" y="735">Caution: If the user attempts to inspect or modify the product in any way</text>
    <text class="info-item" x="1141" y="745">we don't guarantee the performance of the product. Specifications and</text>
    <text class="info-item" x="1141" y="755">design are subject to possible modification notice due to improvements.</text>

    <text class="info-item" x="1141" y="776">Once specific place to be left for Bar Code, manufacturer information</text>
    <text class="info-item" x="1141" y="786">and Certificate Symbols (Picture for reference)</text>

    <text class="info-head" x="1141" y="808">COMPANY NAME HERE</text>
    <text class="info-item" x="1141" y="821">Built for long sessions with clear sound, soft padding and a sturdy frame that</text>
    <text class="info-item" x="1141" y="831">holds its shape. Works with PC, console and mobile devices through a standard</text>
    <text class="info-item" x="1141" y="841">connector. Keep away from moisture and direct heat. Clean the earpads gently</text>
    <text class="info-item" x="1141" y="851">with a dry cloth and store the headset in this box when it is not in use to</text>
    <text class="info-item" x="1141" y="861">protect the cable and drivers. Check the volume before each session and take</text>
    <text class="info-item" x="1141" y="871">regular breaks during long play to rest your ears and stay comfortable.</text>

    <rect x="1138" y="902" width="139" height="48" fill="var(--white)"/>
    <text class="placeholder-label" x="1207" y="929" text-anchor="middle">ICONS</text>
  </g>
</svg>
</body>
</html>
```